Online Rug Store needs Clearance Banner

Website is: Lanternfield Carpets and Home
You can access it at: www.lanternfieldcarpetsandhome.com and login (top right) with password: trazok

*** update: When creating banners for my site, you have permission to use images from www.velbora.com, but ONLY for this project. The images/artwork are copyright allowable for use on www.lanternfieldcarpetsandhome.com projects.***

We need a home page banner sized 1000 wide x 500 tall pixels to promote a "Clearance Sale" on rugs. The banner can state:

1. Clearance Sale
2. Now in progress
3. Save an extra 20% with coupon code 'Mint20'
4. Ends March 31st
5. Plus Free Shipping and 30 day returns.

We prefer a banner that appears hand-drawn and artistic, not commercially produced. It is OK to use a room scene image, rug images, or just a colored/textured background with text and no images. Your choice.

Flat graphics with no shadows and 3-D effect preferred.
Attached is are 3 logo options, as well as an example banner with handcrafted, artistic styling that we prefer.

Target Market(s)

This should be an eye-catching banner to showcase a very urgent promotion. Consider using colors of red, white, gold, and black to make a strong statement on the home page.

Industry/Entity Type

Home And Garden

Requirements
Must have
• Winner must provide Photoshop editable file format (.psd format) including layers that can be edited.
Nice to have
• Hand-drawn, stenciled, scribbled, artistic graphics and fonts is nice because we sell rugs that are made by hand.
Should not have
• little to no shadowing. Avoid computerized graphics.

```html
<!DOCTYPE html>
<html lang="en">
<head>
<meta charset="utf-8">
<title>Clearance Sale – Lanternfield Carpets and Home</title>
<link rel="stylesheet" href="https://fonts.googleapis.com/css2?family=Sniglet:wght@400;800&family=Fredericka+the+Great&family=Short+Stack&display=swap">
<style>
  :root {
    --rug-red: #7a2218;
    --rug-gold: #b38a45;
    --wood-light: #d4a877;
    --wood-mid: #b07b4c;
    --wood-dark: #6e4026;
    --ink-brown: #3b1a0d;
    --ink-black: #1c0f09;
    --white: #ffffff;
    --olive: #6e6a1f;
    --accent-red: #d7261c;
    --logo-red: #8a1e14;
  }
  html, body {
    margin: 0;
    padding: 0;
    width: 1200px;
    height: 600px;
    overflow: hidden;
  }
  .banner {
    position: relative;
    width: 1200px;
    height: 600px;
    overflow: hidden;
    font-family: "Sniglet", sans-serif;
  }
  .rug-backdrop {
    position: absolute;
    inset: 0;
    background: radial-gradient(ellipse at 50% 55%, var(--rug-red) 0%, #8b3020 55%, var(--rug-gold) 100%);
  }
  .wood-slab {
    position: absolute;
    inset: 0;
    width: 1200px;
    height: 600px;
  }
  .headline {
    position: absolute;
    top: 22px;
    left: 0;
    width: 1260px;
    margin: 0;
    text-align: center;
    white-space: nowrap;
    font-weight: 400;
    font-size: 76px;
    line-height: 1;
    color: var(--ink-brown);
  }
  .headline .sale { color: var(--ink-black); }
  .status {
    position: absolute;
    top: 112px;
    left: 342px;
    margin: 0;
    white-space: nowrap;
    font-family: "Fredericka the Great", serif;
    font-size: 38px;
    line-height: 1.2;
    color: var(--white);
  }
  .offer {
    position: absolute;
    top: 192px;
    left: 150px;
    width: 760px;
    margin: 0;
    text-align: center;
    white-space: nowrap;
    font-weight: 400;
    font-size: 48px;
    line-height: 60px;
    color: var(--white);
  }
  .offer .highlight { color: var(--olive); }
  .brand {
    position: absolute;
    top: 358px;
    left: 252px;
    display: flex;
    align-items: center;
    gap: 12px;
  }
  .brand-mark {
    width: 40px;
    height: 40px;
    background: var(--logo-red);
  }
  .brand-name {
    font-weight: 400;
    font-size: 20px;
    line-height: 1.15;
    white-space: nowrap;
    color: var(--ink-black);
  }
  .perks {
    position: absolute;
    top: 336px;
    left: 542px;
    width: 370px;
    margin: 0;
    text-align: right;
    white-space: nowrap;
    font-family: "Short Stack", cursive;
    font-size: 23px;
    line-height: 38px;
    color: var(--ink-brown);
  }
  .perks .number { color: var(--accent-red); }
  .deadline {
    position: absolute;
    top: 428px;
    left: 632px;
    margin: 0;
    white-space: nowrap;
    font-family: "Short Stack", cursive;
    font-size: 33px;
    line-height: 1.2;
    color: var(--white);
  }
  .deadline sup {
    font-size: 18px;
    color: var(--accent-red);
  }
</style>
</head>
<body>
<main class="banner">
  <div class="rug-backdrop" role="img" aria-label="Hand-knotted oriental rug in deep red with gold floral border"></div>

  <svg class="wood-slab" viewBox="0 0 1200 600" role="img" aria-label="Cross-section slab of natural wood with growth rings">
    <defs>
      <radialGradient id="woodGrain" cx="48%" cy="45%" r="60%">
        <stop offset="0%" stop-color="#b07b4c"/>
        <stop offset="55%" stop-color="#d4a877"/>
        <stop offset="85%" stop-color="#b07b4c"/>
        <stop offset="100%" stop-color="#6e4026"/>
      </radialGradient>
    </defs>
    <path fill="url(#woodGrain)" d="M170,22 C330,-18 700,-4 910,12 C1070,24 1150,120 1128,250 C1110,330 1032,362 1000,420 C960,520 880,560 760,584 C620,604 480,562 380,540 C260,516 150,470 130,382 C112,302 162,242 142,172 C122,102 118,40 170,22 Z"/>
  </svg>

  <h1 class="headline">Clearance <span class="sale">Sale</span></h1>
  <p class="status">Now in progress</p>
  <p class="offer">Save an extra <span class="highlight">20%</span><br>with coupon code <span class="highlight">'Mint20'</span></p>

  <div class="brand">
    <div class="brand-mark"></div>
    <div class="brand-name">Lanternfield<br>Carpets and Home</div>
  </div>

  <p class="perks">Plus Free Shipping and<br><span class="number">30</span> day returns.</p>
  <p class="deadline">Ends March 31<sup>st</sup></p>
</main>
</body>
</html>
```